Hollowbrook Renderworks Wordpress Design

I would like a design for my friends company. He has just had his logo designed and really likes the following website.

www.tbr-skimcoat.co.uk

Something similar to this design would be ideal but open to additional ideas. The website shown has all the relevant content.

We have 20 years of experience and can provide a number of photos for work we have done.

More photos will be provided upon request.

Target Market(s)

Homeowners

Industry/Entity Type

Trade

Font styles to use
Sans Serif

Colors
3176b5
85cae6
85abd2
eaf1f7

Requirements
Must have
• look at www.tbr-skimcoat.co.uk
Nice to have
Should not have
• N/A

```html
<!DOCTYPE html>
<html lang="en">
<head>
<meta charset="utf-8">
<title>Hollowbrook Renderworks</title>
<link href="https://fonts.googleapis.com/css2?family=Roboto:wght@300;400;500;700&family=Roboto+Condensed:wght@400;700&display=swap" rel="stylesheet">
<style>
:root{
  --blue:#3176b5;
  --blue-dark:#2a65a0;
  --sky:#85cae6;
  --steel:#85abd2;
  --mist:#eaf1f7;
  --ink:#333;
  --text:#555;
  --grey-band:#f3f3f3;
  --black:#111;
  --white:#fff;
}
*{margin:0;padding:0;box-sizing:border-box}
html,body{width:1200px;height:2695px;overflow:hidden}
body{font-family:"Roboto",Arial,sans-serif;color:var(--text);background:var(--white);position:relative}
section,header,footer{position:absolute;left:0;width:1200px}

/* top bar */
.topbar{top:0;height:32px;background:var(--blue);color:var(--white);font-size:14px}
.topbar .contact{position:absolute;left:88px;top:8px;display:flex;gap:34px;align-items:center}
.topbar .contact span{display:flex;align-items:center;gap:8px}
.topbar .social{position:absolute;right:88px;top:10px;display:flex;gap:4px}
.topbar .social i{display:block;width:12px;height:12px;background:var(--white);border-radius:2px;opacity:.9}

/* header */
.masthead{top:32px;height:119px;background:var(--white)}
.brand{position:absolute;left:88px;top:38px;display:flex;align-items:center;gap:10px;color:var(--blue);font-weight:500;font-size:22px;line-height:26px;letter-spacing:1.5px}
.brand .mark{width:14px;height:14px;background:var(--blue)}
.nav{position:absolute;top:60px;left:0;font-size:16px;color:var(--ink)}
.nav a{position:absolute;white-space:nowrap;color:var(--ink);text-decoration:none}
.nav a.active{color:var(--blue)}

/* hero */
.hero{top:151px;height:510px;background:linear-gradient(100deg,#8d7a66 0%,#b9a996 30%,#d7cdbf 55%,#a58f77 80%,#6f5c4a 100%)}
.hero .beam{position:absolute;left:0;top:0;width:1200px;height:150px;background:linear-gradient(180deg,rgba(70,50,35,.55),rgba(70,50,35,0))}
.hero h1{position:absolute;right:88px;top:206px;font-family:"Roboto Condensed",Arial,sans-serif;font-weight:700;font-size:52px;color:var(--white);letter-spacing:.5px}
.hero .lede{position:absolute;right:88px;top:270px;font-family:"Roboto Condensed",Arial,sans-serif;font-size:28px;color:var(--white)}
.hero .cta{position:absolute;left:946px;top:321px;width:166px;height:49px;background:var(--blue);color:var(--white);font-size:16px;font-weight:500;display:flex;align-items:center;justify-content:center;border-radius:3px}
.hero .pager{position:absolute;left:1042px;top:434px;display:flex;gap:2px}
.hero .pager span{width:24px;height:27px;background:#222;color:var(--white);display:flex;align-items:center;justify-content:center;font-size:14px}

/* welcome */
.welcome{top:661px;height:465px}
.section-title{position:absolute;left:0;width:1200px;text-align:center;font-size:28px;line-height:34px;color:var(--ink);font-weight:400}
.section-title b{color:var(--blue);font-weight:400}
.welcome .intro{position:absolute;left:90px;top:86px;width:1020px;text-align:center;font-size:13px;line-height:21px;color:var(--text)}
.service{position:absolute;top:186px;width:220px;text-align:center}
.service .badge{width:110px;height:110px;margin:0 auto;border-radius:50%;background:var(--white);box-shadow:0 0 0 1px #ddd;display:flex;align-items:center;justify-content:center}
.service .badge div{width:96px;height:96px;border-radius:50%;background:var(--blue);display:flex;align-items:center;justify-content:center}
.service h3{margin-top:26px;font-weight:400;font-size:16px;color:var(--ink)}
.service p{margin-top:10px;font-size:13px;line-height:18px;color:var(--text)}
.chevron{position:absolute}

/* video */
.video-tips{top:1126px;height:424px;background:linear-gradient(135deg,var(--blue-dark),var(--blue) 50%,#3b80c0)}
.player{position:absolute;left:88px;top:54px;width:480px;height:295px;background:var(--white);padding:12px}
.player .screen{width:456px;height:271px;background:linear-gradient(180deg,#7fb0dd 0%,#c9d4dd 45%,#5a4a3c 75%,#3a3530 100%);position:relative}
.player .controls{position:absolute;left:0;bottom:0;width:456px;height:26px;background:#111}
.player .play{position:absolute;left:198px;top:100px}
.video-tips h2{position:absolute;left:594px;top:58px;font-size:25px;font-weight:500;color:var(--white)}
.video-tips h4{position:absolute;left:594px;top:92px;font-size:20px;font-weight:400;color:var(--white)}
.video-tips .copy{position:absolute;left:594px;top:128px;width:516px;font-size:12px;line-height:21px;color:var(--white);text-align:justify}
.video-tips .more{position:absolute;left:594px;top:307px;width:105px;height:36px;border:1px solid var(--white);border-radius:3px;color:var(--white);font-size:13px;display:flex;align-items:center;justify-content:center}

/* recent work */
.recent{top:1550px;height:426px}
.tile{position:absolute;top:127px;width:248px;height:243px}
.tile.feature{background:var(--blue);color:var(--white);text-align:center}
.tile.feature h3{margin-top:36px;font-size:27px;font-weight:500}
.tile.feature p{margin:12px 22px 0;font-size:14px;line-height:22px;text-align:justify}
.tile.feature .tools{position:absolute;left:0;width:248px;top:180px;display:flex;justify-content:center;gap:80px}

/* testimonials */
.testimonials{top:1976px;height:291px;background:var(--grey-band)}
.testimonials .section-title{top:40px;color:var(--blue)}
.quote{position:absolute;top:110px;width:480px;height:140px}
.quote .avatar{position:absolute;left:0;top:0;width:94px;height:94px;border-radius:50%;background:radial-gradient(circle at 50% 40%,#e6c3a6,#b48b6d);border:4px solid var(--white)}
.quote blockquote{position:absolute;left:129px;top:0;width:312px;font-size:12.5px;line-height:22px;color:var(--text)}
.quote .mk{position:absolute;font-size:26px;line-height:26px;color:#999;font-family:Georgia,serif}
.quote .who{position:absolute;left:129px;top:96px;font-size:11px;line-height:14px;font-weight:700;color:var(--blue);white-space:nowrap}
.quote .role{position:absolute;left:129px;top:117px;font-size:12.5px;line-height:16px;color:var(--text);white-space:nowrap}

/* partners */
.partners{top:2267px;height:125px}
.partners i{position:absolute;top:54px;height:34px;background:#c7c7c7;border-radius:3px}

/* footer */
.footer{top:2392px;height:221px;background:var(--blue);color:var(--white)}
.footer h5{position:absolute;top:37px;font-size:15px;font-weight:500;letter-spacing:.3px}
.footer ul{position:absolute;left:92px;top:76px;list-style:none;font-size:12px;line-height:25px}
.footer ul li::before{content:"▸ ";font-size:10px}
.footer .txt{position:absolute;font-size:12px;line-height:18px}
.footer .signup{position:absolute;left:905px;top:118px;display:flex}
.footer .signup span{width:145px;height:30px;background:var(--white);color:#888;font-size:11px;padding:8px 10px}
.footer .signup b{width:57px;height:30px;background:#111;font-weight:400;font-size:12px;display:flex;align-items:center;justify-content:center}
.footer .rings{position:absolute;left:905px;top:166px;display:flex;gap:18px}
.footer .rings i{width:30px;height:30px;border:2px solid var(--white);border-radius:50%}
.legal{top:2613px;height:82px;background:var(--black);color:var(--white);font-size:12px;text-align:center;line-height:82px}
</style>
</head>
<body>

<header class="topbar">
  <div class="contact">
    <span><svg width="12" height="12" viewBox="0 0 24 24"><path fill="#fff" d="M6.6 10.8a15 15 0 0 0 6.6 6.6l2.2-2.2c.3-.3.7-.4 1-.2 1.1.4 2.3.6 3.6.6.6 0 1 .4 1 1V20c0 .6-.4 1-1 1C10.6 21 3 13.4 3 4c0-.6.4-1 1-1h3.5c.6 0 1 .4 1 1 0 1.3.2 2.5.6 3.6.1.3 0 .7-.2 1z"/></svg>(555) 214-7730</span>
    <span><svg width="14" height="11" viewBox="0 0 24 18"><rect width="24" height="18" rx="2" fill="#fff"/><path d="M1 2l11 8 11-8" stroke="#3176b5" stroke-width="2" fill="none"/></svg>hello@hollowbrookrender.com</span>
  </div>
  <div class="social"><i></i><i></i><i></i><i></i><i></i></div>
</header>

<header class="masthead">
  <div class="brand"><span class="mark"></span><span>HOLLOWBROOK<br>RENDERWORKS</span></div>
  <nav class="nav">
    <a class="active" style="left:526px">HOME</a>
    <a style="left:614px">ABOUT US</a>
    <a style="left:727px">SERVICES</a>
    <a style="left:844px">NEWS &amp; UPDATES</a>
    <a style="left:1018px">CONTACT US</a>
  </nav>
</header>

<section class="hero" role="img" aria-label="Photograph of a plasterer working in a stripped-back room with exposed ceiling beams">
  <div class="beam"></div>
  <h1>NATIONWIDE PLASTERING</h1>
  <p class="lede">porro quisquam est qui dolorem ipsum quia dolor</p>
  <div class="cta">GET START NOW</div>
  <div class="pager"><span>‹</span><span>›</span></div>
</section>

<section class="welcome">
  <h2 class="section-title" style="top:42px">WELCOME TO <b>HOLLOWBROOK</b></h2>
  <p class="intro">Lorem Ipsum has been the industry's standard dummy text ever since the 1500s, when an unknown printer took a galley of type and scrambled it to make a type specimen book. It has survived not only five centuries, but also the leap into electronic typesetting, remaining essentially unchanged. It was popularised in the 1960s with the release of Letraset sheets containing Lorem Ipsum passages, and more recently with desktop publishing software like Aldus PageMaker including versions of Lorem Ipsum.</p>

  <svg class="chevron" style="left:66px;top:268px" width="20" height="36" viewBox="0 0 20 36"><path d="M18 2L3 18l15 16" stroke="#bbb" stroke-width="2" fill="none"/></svg>
  <svg class="chevron" style="left:1114px;top:268px" width="20" height="36" viewBox="0 0 20 36"><path d="M2 2l15 16L2 34" stroke="#bbb" stroke-width="2" fill="none"/></svg>

  <div class="service" style="left:102px">
    <div class="badge"><div><svg width="30" height="36" viewBox="0 0 30 36"><rect x="4" y="2" width="22" height="32" fill="#fff"/><g fill="#3176b5"><rect x="8" y="6" width="4" height="4"/><rect x="13" y="6" width="4" height="4"/><rect x="18" y="6" width="4" height="4"/><rect x="8" y="12" width="4" height="4"/><rect x="13" y="12" width="4" height="4"/><rect x="18" y="12" width="4" height="4"/><rect x="8" y="18" width="4" height="4"/><rect x="13" y="18" width="4" height="4"/><rect x="18" y="18" width="4" height="4"/><rect x="12" y="26" width="6" height="8"/></g></svg></div></div>
    <h3>RENDERING</h3><p>Custom web solutions for<br>corporate use</p>
  </div>
  <div class="service" style="left:361px">
    <div class="badge"><div><svg width="40" height="40" viewBox="0 0 40 40"><circle cx="20" cy="20" r="15" stroke="#fff" stroke-width="7" fill="none"/><circle cx="20" cy="20" r="15" stroke="#3176b5" stroke-width="7" stroke-dasharray="6 17.6" stroke-dashoffset="3" fill="none" opacity=".5"/></svg></div></div>
    <h3>SKIMMING</h3><p>Solutions for monitoring, analysis<br>and management</p>
  </div>
  <div class="service" style="left:619px">
    <div class="badge"><div><svg width="40" height="36" viewBox="0 0 40 36"><circle cx="15" cy="20" r="9" stroke="#fff" stroke-width="5" stroke-dasharray="3 2.6" fill="none"/><circle cx="15" cy="20" r="6" fill="#fff"/><circle cx="15" cy="20" r="2.5" fill="#3176b5"/><circle cx="29" cy="9" r="5" fill="#fff"/><circle cx="29" cy="9" r="2" fill="#3176b5"/></svg></div></div>
    <h3>REPOINTING</h3><p>Implementation of any web<br>oriented ideas</p>
  </div>
  <div class="service" style="left:878px">
    <div class="badge"><div><svg width="38" height="38" viewBox="0 0 38 38"><path d="M6 32L22 16" stroke="#fff" stroke-width="6" stroke-linecap="round"/><circle cx="26" cy="12" r="8" fill="#fff"/><circle cx="29" cy="9" r="3.5" fill="#3176b5"/></svg></div></div>
    <h3>CHIMNEY REPAIRS</h3><p>Custom solutions for busi-<br>ness automation</p>
  </div>
</section>

<section class="video-tips">
  <div class="player">
    <div class="screen" role="img" aria-label="Video still of a timber-framed house against a blue sky">
      <svg class="play" width="60" height="60" viewBox="0 0 60 60"><circle cx="30" cy="30" r="28" fill="rgba(0,0,0,.55)"/><path d="M24 18l18 12-18 12z" fill="#fff"/></svg>
      <div class="controls">
        <svg width="456" height="26" viewBox="0 0 456 26"><circle cx="16" cy="13" r="6" stroke="#fff" stroke-width="1.5" fill="none"/><rect x="38" y="9" width="6" height="8" fill="#d33"/><rect x="50" y="12" width="44" height="2" fill="#777"/><rect x="100" y="12" width="216" height="2" fill="#555"/><rect x="100" y="12" width="85" height="2" fill="#d33"/><text x="322" y="17" fill="#ccc" font-size="10" font-family="Roboto,Arial,sans-serif">01:30 / 04:55</text><rect x="394" y="8" width="12" height="9" stroke="#fff" fill="none"/><circle cx="432" cy="13" r="5" fill="#fff"/></svg>
      </div>
    </div>
  </div>
  <h2>HOLLOWBROOK RENDERWORKS'S</h2>
  <h4>MONTHLY VIDEO TIPS</h4>
  <div class="copy">
    <p>Lorem Ipsum has been the industry's standard dummy text ever since the 1500s, when an unknown printer took a galley of type and scrambled it to make a type specimen book. It has survived not only five centuries, but also the leap into electronic typesetting, remaining essentially unchanged. It was popularised in the 1960s with the release of Letraset sheets</p>
    <p style="margin-top:10px">Lorem Ipsum passages, and more recently with desktop publishing software like Aldus PageMaker including versions of Lorem Ipsum.Lorem Ipsum has been the industry's standard dummy text ever since the 1500s, when an unknown printer took a galley of type and scram-</p>
  </div>
  <div class="more">Read More »</div>
</section>

<section class="recent">
  <h2 class="section-title" style="top:48px">HOLLOWBROOK RENDERWORKS'S <b>RECENT WORK?</b></h2>
  <div class="tile" style="left:88px;background:linear-gradient(180deg,#b5a28c,#8c7762 60%,#5e4f42)" role="img" aria-label="Photo of a rounded stone tower with rendered window surrounds"></div>
  <div class="tile feature" style="left:345px">
    <h3>PLASTERING</h3>
    <p>Neque porro quisquam est qui dolorem ipsum quia dolor sit amet,Neque porro quisquam</p>
    <div class="tools">
      <svg width="24" height="24" viewBox="0 0 24 24"><circle cx="10" cy="10" r="7" stroke="#fff" stroke-width="3" fill="none"/><path d="M15 15l7 7" stroke="#fff" stroke-width="3.5" stroke-linecap="round"/></svg>
      <svg width="24" height="24" viewBox="0 0 24 24"><rect x="1" y="9" width="13" height="7" rx="3.5" transform="rotate(45 7.5 12.5)" stroke="#fff" stroke-width="2.5" fill="none"/><rect x="10" y="8" width="13" height="7" rx="3.5" transform="rotate(45 16.5 11.5)" stroke="#fff" stroke-width="2.5" fill="none"/></svg>
    </div>
  </div>
  <div class="tile" style="left:603px;background:linear-gradient(180deg,#9fc3e6 0%,#b49c82 35%,#8a6f55 75%,#6a5646)" role="img" aria-label="Photo of a stone-faced extension under construction with a timber porch"></div>
  <div class="tile" style="left:862px;background:linear-gradient(180deg,#d7cfc4 0%,#b89974 50%,#9c7b5a 75%,#c9bfb0)" role="img" aria-label="Photo of a brick bay window with fresh render at its base"></div>
</section>

<section class="testimonials">
  <h2 class="section-title">TESTIMONIALS</h2>
  <svg class="chevron" style="left:62px;top:150px" width="18" height="34" viewBox="0 0 18 34"><path d="M16 2L3 17l13 15" stroke="#bbb" stroke-width="2" fill="none"/></svg>
  <svg class="chevron" style="left:1116px;top:150px" width="18" height="34" viewBox="0 0 18 34"><path d="M2 2l13 15L2 32" stroke="#bbb" stroke-width="2" fill="none"/></svg>

  <div class="quote" style="left:106px">
    <div class="avatar" role="img" aria-label="Portrait of the client"></div>
    <span class="mk" style="left:115px;top:-6px">“</span>
    <blockquote>Lorem Ipsum has been the industry's standard dummy text ever since the 1500s, when an unknown printer took a galley of type and scrambled it to make</blockquote>
    <span class="mk" style="left:390px;top:50px">„</span>
    <div class="who">TOBIN MARECK</div>
    <div class="role">Marketing Executive</div>
  </div>
  <div class="quote" style="left:658px">
    <div class="avatar" role="img" aria-label="Portrait of the client"></div>
    <span class="mk" style="left:115px;top:-6px">“</span>
    <blockquote>Lorem Ipsum has been the industry's standard dummy text ever since the 1500s, when an unknown printer took a galley of type and scrambled it to make</blockquote>
    <span class="mk" style="left:390px;top:50px">„</span>
    <div class="who">TOBIN MARECK</div>
    <div class="role">Marketing Executive</div>
  </div>
</section>

<section class="partners" aria-label="Partner badges">
  <i style="left:126px;width:66px"></i>
  <i style="left:252px;width:112px"></i>
  <i style="left:427px;width:94px"></i>
  <i style="left:595px;width:110px"></i>
  <i style="left:792px;width:84px"></i>
  <i style="left:950px;width:118px"></i>
</section>

<footer class="footer">
  <h5 style="left:92px">LINKS</h5>
  <ul>
    <li>Customer Support</li><li>Documentation</li><li>Resources</li><li>General FAQs</li><li>Shortcodes</li>
  </ul>
  <h5 style="left:300px">NATIONWIDE PLASTERING</h5>
  <p class="txt" style="left:300px;top:74px;width:230px;text-align:justify">Lorem Ipsum has been the industry's standard dummy text ever since the 1500s, when an unknown printer took</p>
  <p class="txt" style="left:300px;top:136px;width:230px;text-align:justify">a galley of type and scrambled it to make a type specimen book. It has survived not only five centuries, but also the leap into electronic typeset-</p>
  <h5 style="left:650px">GET IN TOUCH</h5>
  <p class="txt" style="left:650px;top:82px">Address : 48 Millrace Lane,<br>Ashford Vale</p>
  <p class="txt" style="left:650px;top:132px">Phone : 555 380 1926</p>
  <p class="txt" style="left:650px;top:168px">Email : hello@hollowbrookrender.com</p>
  <h5 style="left:905px">NEWSLETTER</h5>
  <p class="txt" style="left:905px;top:74px;width:200px">Your about us information would fit here nicely.</p>
  <div class="signup"><span>Email address</span><b>Submit</b></div>
  <div class="rings"><i></i><i></i><i></i></div>
</footer>

<footer class="legal">Copyright © 2016. All Rights Reserved</footer>

</body>
</html>
```